I need a flyer for my pageant/event. The theme is based off Brenwick's Grand Runway Star so think "fashion show" "models" etc.
I have uploaded two photos that need to be on the flyer. The photo labeled "Dale Fenwick- Miss Velvet Starlight Regalia 2025" needs to be a bit larger than the other photo.
The following needs to be on the flyer:
Marigold Productions Presents
Miss Velvet Starlight Regalia 2026
Sunday, July 12, 2026 at Halvern Hall for Performance- 5pm
When including the photos, please also add (underneath the photos) the title of the photos (which is their name and their current title)
The flashier the better with this flyer.

```html
<!DOCTYPE html>
<html lang="en">
<head>
<meta charset="UTF-8">
<title>Miss Velvet Starlight Regalia 2026 – Flyer</title>
<link href="https://fonts.googleapis.com/css2?family=Josefin+Sans:wght@300;400&family=Playfair+Display:wght@700&display=swap" rel="stylesheet">
<style>
  :root {
    --page-bg: #3b3b3d;
    --ink-white: #f4f4f6;
    --ink-dark: #1a1a1c;
    --silver-light: #eceef2;
    --silver-mid: #a9acb4;
    --silver-deep: #5d6068;
    --night: #040405;
    --rule: #c9cbd0;
  }
  * { margin: 0; padding: 0; box-sizing: border-box; }
  html, body {
    width: 1200px; height: 881px; overflow: hidden;
    background: var(--page-bg);
  }
  .flyer {
    position: absolute; left: 350px; top: 60px;
    width: 500px; height: 761px; overflow: hidden;
    background:
      radial-gradient(circle 70px at 95px 300px, rgba(255,255,255,.55), transparent 70%),
      radial-gradient(circle 90px at 130px 110px, rgba(255,255,255,.7), transparent 70%),
      radial-gradient(circle 80px at 330px 80px, rgba(255,255,255,.5), transparent 70%),
      radial-gradient(circle 75px at 420px 250px, rgba(255,255,255,.45), transparent 70%),
      radial-gradient(circle 60px at 250px 260px, rgba(255,255,255,.4), transparent 70%),
      linear-gradient(180deg, #c4c6cb 0%, #a4a7ae 22%, #7a7d84 38%, #3a3c41 52%, #17181b 66%, #0d0d0f 80%, var(--night) 92%);
    font-family: "Josefin Sans", sans-serif;
  }
  .backdrop-sparkle { position: absolute; inset: 0; width: 500px; height: 761px; }
  .presenter {
    position: absolute; top: 22px; left: 0; width: 100%;
    text-align: center; font-size: 15px; letter-spacing: 1.4px;
    color: var(--ink-dark); z-index: 4;
  }
  .photo-caption {
    position: absolute; color: var(--ink-dark); letter-spacing: .2px; z-index: 4;
  }
  .caption-lead { left: 158px; top: 57px; font-size: 13px; }
  .caption-second { left: 262px; top: 133px; font-size: 11px; }
  .photo { position: absolute; border-radius: 42% 42% 10% 10%; }
  .photo-lead {
    left: 82px; top: 78px; width: 230px; height: 390px;
    background: linear-gradient(180deg, #eee9e3 0%, #d5b3b0 28%, #6e2437 55%, #3e6d4a 100%);
    z-index: 2;
  }
  .photo-second {
    left: 262px; top: 150px; width: 215px; height: 290px;
    background: linear-gradient(180deg, #d8b46a 0%, #e7c49c 35%, #4a3a30 70%, #2a211c 100%);
    z-index: 1;
  }
  .title-main {
    position: absolute; left: 48px; top: 388px; width: 420px;
    font-family: "Playfair Display", serif; font-weight: 700;
    font-size: 80px; line-height: 1; letter-spacing: -1px; white-space: nowrap;
    background: linear-gradient(180deg, #ffffff 0%, var(--silver-light) 30%, var(--silver-deep) 52%, #ffffff 72%, var(--silver-mid) 100%);
    -webkit-background-clip: text; background-clip: text; color: transparent;
    filter: drop-shadow(0 2px 3px rgba(0,0,0,.7));
    z-index: 3;
  }
  .title-sub {
    position: absolute; left: 51px; top: 511px;
    font-size: 18px; letter-spacing: 3.5px; color: var(--silver-light); z-index: 3;
  }
  .title-year {
    position: absolute; left: 174px; top: 536px;
    font-size: 31px; letter-spacing: 3px; font-weight: 300;
    color: var(--silver-light); z-index: 3;
  }
  .rule { position: absolute; left: 45px; height: 1.5px; background: var(--rule); }
  .rule-top { top: 602px; width: 429px; }
  .rule-bottom { top: 654px; width: 406px; }
  .event-date {
    position: absolute; left: 45px; top: 610px;
    font-size: 37px; font-weight: 300; line-height: 1.1;
    color: var(--ink-white); letter-spacing: .3px; white-space: nowrap;
  }
  .event-venue {
    position: absolute; left: 45px; top: 665px;
    font-size: 18px; color: var(--ink-white); letter-spacing: .4px; white-space: nowrap;
  }
</style>
</head>
<body>
  <main class="flyer">
    <svg class="backdrop-sparkle" viewBox="0 0 500 761" aria-hidden="true">
      <g fill="#d9dbe0" opacity=".85">
        <rect x="120" y="60" width="14" height="6" transform="rotate(-20 127 63)"/>
        <rect x="420" y="75" width="30" height="12" transform="rotate(-25 435 81)"/>
        <rect x="355" y="110" width="10" height="5" transform="rotate(30 360 112)"/>
        <rect x="60" y="130" width="12" height="5" transform="rotate(50 66 132)"/>
        <rect x="450" y="200" width="9" height="4" transform="rotate(-40 454 202)"/>
        <rect x="455" y="300" width="16" height="6" transform="rotate(35 463 303)"/>
        <rect x="30" y="260" width="10" height="4" transform="rotate(-15 35 262)"/>
        <rect x="215" y="40" width="8" height="4" transform="rotate(60 219 42)"/>
        <rect x="475" y="150" width="12" height="5" transform="rotate(10 481 152)"/>
      </g>
      <g stroke="#ffffff" stroke-width=".7" opacity=".45" fill="none">
        <line x1="40" y1="95" x2="110" y2="40"/>
        <line x1="300" y1="20" x2="380" y2="60"/>
        <line x1="20" y1="330" x2="80" y2="290"/>
        <line x1="400" y1="330" x2="470" y2="280"/>
      </g>
      <g fill="#ffffff">
        <path d="M175 500 l2 -12 l2 12 l12 2 l-12 2 l-2 12 l-2 -12 l-12 -2 z"/>
        <path d="M430 470 l1.5 -9 l1.5 9 l9 1.5 l-9 1.5 l-1.5 9 l-1.5 -9 l-9 -1.5 z"/>
        <path d="M78 280 l1.5 -8 l1.5 8 l8 1.5 l-8 1.5 l-1.5 8 l-1.5 -8 l-8 -1.5 z"/>
        <path d="M380 250 l1 -6 l1 6 l6 1 l-6 1 l-1 6 l-1 -6 l-6 -1 z"/>
        <circle cx="36" cy="578" r="1.3"/><circle cx="470" cy="430" r="1.3"/>
        <circle cx="478" cy="535" r="1.2"/><circle cx="460" cy="590" r="1"/>
        <circle cx="70" cy="540" r="1"/><circle cx="280" cy="580" r="1"/>
      </g>
    </svg>

    <p class="presenter">MARIGOLD PRODUCTIONS PRESENTS</p>
    <p class="photo-caption caption-lead">DALE FENWICK</p>
    <p class="photo-caption caption-second">TESSA LAROUCHE</p>

    <div class="photo photo-second" role="img" aria-label="Portrait of Tessa Larouche in a gold wig, crown and brown jacket holding a scepter"></div>
    <div class="photo photo-lead" role="img" aria-label="Portrait of Dale Fenwick in a platinum wig, crown and jewelled burgundy bodysuit with rainbow feathers"></div>

    <h1 class="title-main">miss velvet</h1>
    <p class="title-sub">STARLIGHT REGALIA</p>
    <p class="title-year">2026</p>

    <div class="rule rule-top"></div>
    <p class="event-date">SUNDAY, JULY 12, 2026</p>
    <div class="rule rule-bottom"></div>
    <p class="event-venue">AT HALVERN HALL FOR PERFORMANCE – 5PM</p>
  </main>
</body>
</html>
```